Velmorant Commercial Catalog

Velmorant is an innovative and young company seeking to revolutionize and reinvigorate the wood floor refinishing industry. We make hi-tech waterborne wood floor finishes, each raising the bar in the market. We want customers to rethink what they can get out of a wood floor finish, and challenge conventional wisdom.

We see ourselves as visionary, hi-tech, consumer focused, and elite. We strive to bring the Silicon Valley business model and philosophy to the wood floor refinishing industry.

We have products for residential as well as commercial customers. Commercial customers include engineers, architects, facility owners, restaurants, retail stores, etc.

For this project, we want you to create an 8-page commercial catalog. This catalog will be used to promote our line of commercially suitable products. We would like to establish ourselves as the go to provider of commercial finishes, as this segment of the market is untapped.

The design should communicate energy, freshness, professionalism, confidence, and lightheartedness. Clean lines, soothing colors schemes.

Attached is a document to facilitate design. This document includes a draft of the copy we plan to use. This amount of copy, no more but possibly less, needs to fit in the design. The document has descriptions of a basic vision, which are guiding principles, not rules. These are highlighted in yellow on the document.

We have also provided a folder with branded images, such as product shots to place in the design. Some of these may be changing, but will work as placeholders for design purposes. The folder also includes shots of our KorvaShield product in action. This is the focus of the catalog. Incorporation of these is encouraged.

Stock photos are also encouraged where possible. Our vision is just an idea. We encourage creativity and re-imaginings of what we have offered.
Updates

A good link for inspiration: http://www.example-halvig.com/en/grundlinie-pu-katalog-halvig

The word doc has been reattached, as one designer pointed out the file was no longer working.  This is the same file as before if you have downloaded the first attachment.

PixelBazaar is not allowing me to delete the now broken file for some reason.  Please download the word doc dated July 22.

Our deadline is fast approaching. Are there any further questions we can answer for you? All designs should have the inside back cover as a pocket folder designed into it. Just to clarify, all designs should be sized to allow for 8.5 x 11 sheets to be held within this pocket. Thank you for all your ideas and efforts.

Reason: Due to an unexpected absence, feedback was not provided in as timely a manner as we had planned. In order to make up for this inconvenience for designers, the deadline has been extended 5 days.

Reason: Need more time to tweak designs to what we need.

Target Market(s)

Commercial floor owners. Architects. Retail store owners. Engineers

Industry/Entity Type

Residential

Requirements
Must have
• Must have 8 pages
Must Include our Logo (provided)
Must Include copy on attachment
Must include product shots
Must be clean and sophisticated
Calming/relaxing color scheme
Incorporation of at least a few KorvaShield action shots provided

Should not have
• No clip art
No serif fonts
No neon colors

```html
<!DOCTYPE html>
<html lang="en">
<head>
<meta charset="utf-8">
<title>KorvaShield – Features &amp; Benefits</title>
<link rel="stylesheet" href="https://fonts.googleapis.com/css2?family=Jost:ital,wght@0,400;0,500;0,600;1,400&display=swap">
<style>
  :root {
    --paper: #fffbea;
    --ink: #111111;
    --accent: #1ea6df;
    --muted: #8a8a8a;
    --rule: #1a1a1a;
    --wood-light: #a7783f;
    --wood-dark: #4a2e16;
    --room-light: #d9c7a6;
    --room-dark: #8d7860;
  }
  * { box-sizing: border-box; margin: 0; padding: 0; }
  html, body { width: 1200px; height: 785px; overflow: hidden; background: var(--paper); }
  body {
    position: relative;
    font-family: "Jost", "Futura", sans-serif;
    color: var(--ink);
    letter-spacing: -0.25px;
  }
  .page-title {
    position: absolute;
    top: 70px;
    font-size: 18px;
    font-weight: 400;
    letter-spacing: 0.4px;
  }
  .page-title.left { left: 56px; }
  .page-title.right { left: 658px; }

  .product-shot {
    position: absolute;
    left: 132px; top: 162px;
    width: 318px; height: 342px;
    border-radius: 40% 40% 8px 8px / 22% 22% 8px 8px;
    background: radial-gradient(ellipse at 50% 25%, var(--wood-light), var(--wood-dark) 85%);
  }

  .intro-lead {
    position: absolute;
    left: 58px; top: 542px;
    font-size: 9.5px; font-weight: 600;
    color: var(--accent);
  }
  .intro-body {
    position: absolute;
    left: 58px; top: 568px; width: 484px;
    font-size: 9.3px; line-height: 13.6px;
    text-align: justify;
  }

  .page-number {
    position: absolute;
    top: 733px;
    font-size: 11px; font-weight: 600;
  }
  .page-number.left { left: 26px; }
  .page-number.right { left: 1161px; }

  .features {
    position: absolute;
    left: 658px; top: 103px; width: 484px;
    font-size: 9.3px; line-height: 13.4px;
    text-align: justify;
  }
  .features .label { color: var(--accent); font-weight: 600; }
  .features .note { color: var(--muted); font-style: italic; }

  .tagline {
    position: absolute;
    left: 658px; top: 289px; width: 484px;
    font-size: 9.3px; line-height: 13.4px;
  }
  .tagline .product-dot {
    display: inline-block;
    width: 13px; height: 13px;
    border-radius: 50%;
    background: #a0552e;
    vertical-align: -2px;
    margin-right: 2px;
  }

  .spec-table {
    position: absolute;
    left: 701px; top: 335px; width: 410px;
    border-collapse: collapse;
    font-size: 9.8px; line-height: 11.6px;
  }
  .spec-table th {
    background: var(--ink); color: var(--paper);
    font-weight: 500; text-align: left;
    height: 19px; padding: 0 0 0 48px;
  }
  .spec-table th:last-child { padding-left: 0; }
  .spec-table td {
    border-bottom: 1px solid var(--rule);
    vertical-align: top;
    padding: 3px 0 2px 48px;
  }
  .spec-table td:last-child { padding-left: 0; width: 126px; }

  .curing-title {
    position: absolute;
    left: 661px; top: 591px;
    font-size: 9.5px; font-weight: 600;
    color: var(--accent);
  }
  .curing-body {
    position: absolute;
    left: 661px; top: 615px; width: 240px;
    font-size: 9.3px; line-height: 13.4px;
    text-align: justify;
  }

  .action-shot {
    position: absolute;
    left: 910px; top: 579px;
    width: 235px; height: 161px;
    background: linear-gradient(180deg, #efece6 0%, #cfc8bc 45%, var(--room-light) 60%, var(--room-dark) 100%);
  }
</style>
</head>
<body>
  <section class="page page-left">
    <h1 class="page-title left">SPREAD: KORVASHIELD</h1>
    <div class="product-shot" role="img" aria-label="Product shot: rustic three-legged wooden stool with KorvaShield finish"></div>
    <p class="intro-lead">Meet KorvaShield. It’s stronger, faster, and cleaner.</p>
    <p class="intro-body">Instantly cured floors are the next revolution for the flooring industry. Based on five years of intensive development and testing, KorvaShield is Velmorant’s instant cure solution.<br>KorvaShield takes waterborne finishes to the next level. It’s the Velmorant finish you know and love, with the inclusion of photoinitiators. This cutting edge technology allows KorvaShield to cure instantly. By coupling this advancement with our unparalled nanoceramic technology, KorvaShield is quickly becoming the premiere waterborne finish on the market, in more ways than one. With KorvaShield, you really can have it all.</p>
    <span class="page-number left">5</span>
  </section>

  <section class="page page-right">
    <h2 class="page-title right">FEATURES &amp; BENEFITS</h2>
    <p class="features">
      <span class="label">Instant Cure:</span> A KorvaShield job can be completed from sanding to cured in less than a day. This means reduced operational downtime for businesses, and satisfied customers.<br>
      <span class="label">Reduced Early Damage:</span> 90% of floor damage occurs during the curing period, when the finish is most vulnerable. KorvaShield is fully cured when the contractor finishes the job. The floor can withstand full use immediately, without risk of early use damage.<br>
      <span class="label">Unrivaled Durability:</span> Compared to traditional two component finishes, KorvaShield is the toughest, most durable waterborne finish on the market. In testing, floors cured with KorvaShield even match or surpass the durability of factory prefinished flooring.<br>
      <span class="label">Better for Floor Owners and the Environment:</span> KorvaShield is the flagship of green finishes, performing above and beyond even the strictest environmental standards in the industry. <span class="note">(Passes KTVR Standard, Passes CA01350; NMP Free; Solvent Free)</span><br>
      <span class="label">User Friendly Simplicity:</span> KorvaShield only needs to be cured once. Other ultraviolet finishes need to be cured once per coat. Using KorvaShield saves you time and effort.
    </p>
    <p class="tagline"><span class="product-dot" role="img" aria-label="Small KorvaShield product can"></span>KorvaShield – Premium instant cure commercial finish. KorvaShield provides world class protection, and allows immediate return to business activities.</p>

    <table class="spec-table">
      <tr><th>Special Ingredients</th><th>Ceramic Silica</th></tr>
      <tr><td>Recommended Use</td><td>Commercial</td></tr>
      <tr><td>Additional Features</td><td>NMP Free</td></tr>
      <tr><td>Volatile Organic<br>Compound (VOC)</td><td>Maximum of 21 g/L</td></tr>
      <tr><td>Gloss Levels<br>(60 Halden)</td><td>KorvaShield 8 (Ultra Matte)<br>KorvaShield 20 (Satin)<br>KorvaShield 45 (Semi-gloss)<br>KorvaShield 90 (Gloss)</td></tr>
      <tr><td>Flow &amp; Leveling</td><td>Exceptional</td></tr>
      <tr><td>Coverage</td><td>500-600 sq. ft. per gal.</td></tr>
      <tr><td>Dry time (68F, RH 55%)<br>First coat</td><td>1-2 hours</td></tr>
      <tr><td>Full Cure Time</td><td>Immediately after<br>UV Curing</td></tr>
    </table>

    <h3 class="curing-title">Curing KorvaShield</h3>
    <p class="curing-body">KorvaShield is as easy to apply as all other Velmorant waterborne finishes, and extremely safe when applied appropriately. Once applied, the finish is exposed to and instantly cured by ultraviolet light from a portable UV machine. It doesn’t get any faster than that.<br>“Hollowmere Home Ashby Corner employees replacing fixtures while instant curing still underway.”</p>
    <div class="action-shot" role="img" aria-label="Action shot: worker curing a retail store wood floor with a portable UV machine"></div>
    <span class="page-number right">6</span>
  </section>
</body>
</html>
```